Indian Takeaway Menu -

I would like to have double parallel fold A4 sheet menu.
A4 sheet cut in half and attached to the other half to make the sheet 4 small pages long.

Colors
abd036
ffffff

Requirements
Must have
• Please check new attachments - menu size and layout is not correct.
• I would like to add Dark brown colour. A4 sheet folded 4x Menu layout pocket size.
Nice to have
• Dark Brown - Parrot Green and very light Brown

```html
<!DOCTYPE html>
<html lang="en">
<head>
<meta charset="utf-8">
<title>Indian Takeaway Menu – Lamb, Prawn &amp; Vegetarian</title>
<link rel="stylesheet" href="https://fonts.googleapis.com/css2?family=Open+Sans:ital,wght@0,700;0,800;1,700;1,800&family=Roboto+Condensed:wght@400&display=swap">
<style>
  :root {
    --parrot-green: #abd036;
    --green-soft: #d6e893;
    --cream: #f6f8e2;
    --paper: #ffffff;
    --dark-brown: #2a1a0f;
    --chilli-red: #e3202c;
    --text-brown: #3a2a1e;
    --frame: #3c3c3c;
  }
  * { box-sizing: border-box; margin: 0; padding: 0; }
  html, body { width: 1200px; height: 848px; overflow: hidden; background: var(--paper); }
  .canvas { position: relative; width: 1200px; height: 848px; }

  .menu-page {
    position: absolute; left: 299px; top: 11px; width: 605px; height: 818px;
    border: 1px solid var(--frame); overflow: hidden;
    background: linear-gradient(90deg, var(--parrot-green) 0%, var(--green-soft) 16%, var(--cream) 42%, #fbfcf1 70%, var(--paper) 100%);
    font-family: "Open Sans", Arial, sans-serif;
  }

  .section-title {
    position: absolute; left: 28px;
    font-weight: 800; font-size: 30px; line-height: 1; letter-spacing: -0.3px;
    color: var(--dark-brown); text-transform: uppercase; white-space: nowrap;
  }
  .section-title.is-red { color: var(--chilli-red); }
  .section-title.is-veg { font-size: 26px; letter-spacing: -0.5px; }

  .dish { position: absolute; left: 30px; width: 560px; }
  .dish-name {
    font-weight: 800; font-style: italic; font-size: 13.5px; line-height: 1.2;
    color: var(--chilli-red); text-transform: uppercase; white-space: nowrap;
  }
  .allergens { margin-left: 26px; font-style: italic; }
  .dish-price {
    position: absolute; top: 0; left: 453px;
    font-weight: 800; font-style: italic; font-size: 13.5px; line-height: 1.2; color: var(--chilli-red);
  }
  .dish-desc {
    font-family: "Roboto Condensed", "Arial Narrow", sans-serif;
    font-size: 9.3px; line-height: 1.25; color: var(--text-brown); margin-top: 2px;
  }

  .veg .dish { width: 285px; }
  .veg .dish-name { font-size: 12.5px; }
  .veg .dish-price { left: 240px; font-style: normal; font-weight: 700; font-size: 12.5px; }
  .veg .dish-desc { width: 285px; font-size: 8.6px; line-height: 1.15; margin-top: 1px; }

  .column-rule {
    position: absolute; left: 323px; top: 520px; width: 1px; height: 292px;
    background: var(--frame);
  }

  .sides-heading {
    position: absolute; left: 340px; top: 518px;
    font-weight: 800; font-size: 11.5px; line-height: 1.1; color: var(--dark-brown);
    text-transform: uppercase; white-space: nowrap;
  }
  .sides-list { position: absolute; left: 339px; top: 555px; width: 250px; list-style: none; }
  .side-item {
    position: relative;
    font-weight: 800; font-size: 13px; line-height: 18.6px; color: var(--chilli-red); white-space: nowrap;
  }
  .side-item .side-price { position: absolute; left: 181px; top: 0; font-weight: 700; }
</style>
</head>
<body>
<div class="canvas">
  <article class="menu-page">

    <h2 class="section-title" style="top:13px">Lamb Dishes</h2>

    <div class="dish" style="top:56px">
      <p class="dish-name">Lamb Madras</p><span class="dish-price">€10.95</span>
      <p class="dish-desc">The popular dish of madras cooked with plum tomato , degi chilli , coconut and finished with hint of lemon juice.</p>
    </div>
    <div class="dish" style="top:97px">
      <p class="dish-name">Palak Gosht <span class="allergens">3, Y</span></p><span class="dish-price">€10.95</span>
      <p class="dish-desc">Pan-fried lamb pieces cooked with spinach, fresh herbs, ginger and touch of cream</p>
    </div>
    <div class="dish" style="top:138px">
      <p class="dish-name">Lamb Roganjosh</p><span class="dish-price">€10.95</span>
      <p class="dish-desc">Slow cooked tender lamb in kashmiri style with fresh herbs and Himalayan spices.</p>
    </div>
    <div class="dish" style="top:179px">
      <p class="dish-name">Lamb Kohlapuri <span class="allergens">3,4,5</span></p><span class="dish-price">€10.95</span>
      <p class="dish-desc">lamb dish from South Coast of India Flavoured with yoghurt, nuts and coconut.</p>
    </div>
    <div class="dish" style="top:220px">
      <p class="dish-name">Lamb Jalferzi <span class="allergens">3,5</span></p><span class="dish-price">€10.95</span>
      <p class="dish-desc">Lamb, tossed with cubes of onions, peppers flavored with crushed coriander seeds and dry fenugreek with hint of cream.</p>
    </div>
    <div class="dish" style="top:260px">
      <p class="dish-name">Gosht Biryani <span class="allergens">3,5,Y</span></p><span class="dish-price">€11.00</span>
      <p class="dish-desc">Aged rice cooked with tender land brown onions, home made masala and accompanied with curry sauce.</p>
    </div>

    <h2 class="section-title is-red" style="top:297px">Prawn Dishes</h2>

    <div class="dish" style="top:331px">
      <p class="dish-name">Prawn Masala 3</p><span class="dish-price">€11.95</span>
      <p class="dish-desc">Prawns in a smooth creamy sauce flavoured with kasoori methi &amp; tandoori spices</p>
    </div>
    <div class="dish" style="top:368px">
      <p class="dish-name">Prawn Karahi</p><span class="dish-price">€11.95</span>
      <p class="dish-desc">Prawns cooked with peppers, spring onion, Caramelised onion ,tomatoes &amp; whole spices</p>
    </div>
    <div class="dish" style="top:404px">
      <p class="dish-name">Goan Prawn Curry <span class="allergens">3,4,5</span></p><span class="dish-price">€11.95</span>
      <p class="dish-desc">Fisherman`s favourite prawn curry aromatic with coconut , mustard , nuts ,curryleaves and spices from goa's costal area.</p>
    </div>
    <div class="dish" style="top:441px">
      <p class="dish-name">Prawn Bhuna <span class="allergens" style="margin-left:70px">LF</span></p><span class="dish-price">€11.95</span>
      <p class="dish-desc">Prawns cooked in onions &amp; tomato with black pepper to bought together the kick of spices</p>
    </div>
    <div class="dish" style="top:481px">
      <p class="dish-name">Prawn Biryani <span class="allergens">3,6,Y</span></p><span class="dish-price">€11.95</span>
      <p class="dish-desc">Pan fried prawn cooked with egg, green peas &amp; onion served with curry sauce.</p>
    </div>

    <section class="veg">
      <h2 class="section-title is-veg" style="top:516px">Vegetarian Dishes</h2>

      <div class="dish" style="top:558px">
        <p class="dish-name">Shahi Paneer <span class="allergens">3, 5</span></p><span class="dish-price">8.95</span>
        <p class="dish-desc">Indian cheese in semi-dry sauce.</p>
      </div>
      <div class="dish" style="top:588px">
        <p class="dish-name">Subz Maloni Mild.</p><span class="dish-price">8.95</span>
        <p class="dish-desc">Stir fried vegetables with ground spices.</p>
      </div>
      <div class="dish" style="top:618px">
        <p class="dish-name">Dum Wale Aloo <span class="allergens" style="margin-left:6px">3</span></p><span class="dish-price">8.95</span>
        <p class="dish-desc">Potatoes cooked with ginger, garlic, onions, yoghurt,&amp; curry l eave with cumin Flavoured.</p>
      </div>
      <div class="dish" style="top:664px">
        <p class="dish-name">Karahi Paneer <span class="allergens">3</span></p><span class="dish-price">8.95</span>
        <p class="dish-desc">Colorful curry is prepared using homemade Indian cheese (paneer)</p>
      </div>
      <div class="dish" style="top:698px">
        <p class="dish-name">Saag Paneer <span class="allergens">3 , Y,</span></p><span class="dish-price">8.95</span>
        <p class="dish-desc">Pan fried cottage cheese &amp; spinach with kasoori methi &amp; fresh coriander</p>
      </div>
      <div class="dish" style="top:731px">
        <p class="dish-name">Sambhar Vegetable Curry 4, YV</p><span class="dish-price">8.95</span>
        <p class="dish-desc">Vegetable curry cooked with lentil, curry leaves, and mustard seeds</p>
      </div>
      <div class="dish" style="top:761px">
        <p class="dish-name">Vegetable Biryani <span class="allergens" style="margin-left:10px">3,5,Y V</span></p><span class="dish-price">8.95</span>
        <p class="dish-desc">Basmati Rice cooked with vegetables, fresh herbs, spices &amp;<br>fried golden onion. Comes with curry sauce</p>
      </div>
    </section>

    <div class="column-rule"></div>

    <aside>
      <h3 class="sides-heading">Nan Bread &amp; Side Orders<br>All Naan Bread Contains 2,3,6</h3>
      <ul class="sides-list">
        <li class="side-item">Naan<span class="side-price">€2.20</span></li>
        <li class="side-item">Garlic Naan<span class="side-price">€2.50</span></li>
        <li class="side-item">Garlic Chilli Naan<span class="side-price">€3.00</span></li>
        <li class="side-item">Peshwari Naan<span class="side-price">€3.00</span></li>
        <li class="side-item">Keema Naan<span class="side-price">€3.00</span></li>
        <li class="side-item">Coriander Naan.<span class="side-price">2.50</span></li>
        <li class="side-item">Chilli Cheese Naan3<span class="side-price">3.00</span></li>
        <li class="side-item">G.O.C<span class="side-price">€3.00</span></li>
        <li class="side-item">&nbsp;Boiled Basmati.<span class="side-price">€2.00</span></li>
        <li class="side-item">&nbsp;Pilau Rice<span class="side-price">€2.00</span></li>
        <li class="side-item">Lemon Rice.4.<span class="side-price">€3.00</span></li>
        <li class="side-item">&nbsp;Poppodum(2)<span class="side-price">€2.50</span></li>
        <li class="side-item">Riata3<span class="side-price">€2.50</span></li>
      </ul>
    </aside>

  </article>
</div>
</body>
</html>
```